Creative Businesss Card desgin!

Create a business card for our business Gleam window cleaning!
We are open to creative ideas as long as it maintains a professional image.

Target Market(s)

Small Commercial window cleaning clients including car dealerships, strata manager, cafe

Industry/Entity Type

Window Cleaning

Contact Information for Business Card

Daniel Prescott
General Manager
Gleam Window Cleaning

daniel@gleamservices.com.au
pane-care-southbank.com.au
Ph: 1800 GET GLEAM
Mob: 0437 582 061

Colors
fbed22
0392cd

Requirements
Should not have
• Stock window cleaning/ squeegee graphics

```html
<!DOCTYPE html>
<html lang="en">
<head>
<meta charset="utf-8">
<title>Gleam Window Cleaning – Business Card</title>
<link rel="stylesheet" href="https://fonts.googleapis.com/css2?family=Arimo:wght@700&family=Play:wght@700&display=swap">
<style>
  :root {
    --stage: #000000;
    --card: #ffffff;
    --brand-blue: #437de8;
    --brand-yellow: #f3e940;
    --flap-olive: #c2b524;
    --text-blue: #437de8;
  }
  html, body {
    margin: 0;
    padding: 0;
    width: 1200px;
    height: 1200px;
    overflow: hidden;
    background: var(--stage);
  }
  .canvas {
    position: relative;
    width: 1200px;
    height: 1200px;
  }
  .card {
    position: absolute;
    left: 292px;
    width: 540px;
    height: 307px;
    background: var(--card);
    display: block;
  }
  .card--front { top: 192px; }
  .card--back { top: 644px; }
  .panel { fill: var(--brand-blue); }
  .swoosh { fill: var(--brand-yellow); }
  .flap-shade { fill: var(--flap-olive); }
  .brand-name {
    font-family: "Arimo", Arial, sans-serif;
    font-weight: 700;
    fill: var(--brand-yellow);
  }
  .brand-tagline {
    font-family: "Arimo", Arial, sans-serif;
    font-weight: 700;
    fill: var(--brand-yellow);
  }
  .placeholder {
    font-family: "Play", "Trebuchet MS", sans-serif;
    font-weight: 700;
    fill: var(--text-blue);
  }
</style>
</head>
<body>
<main class="canvas">

  <!-- Front of card -->
  <svg class="card card--front" viewBox="0 0 540 307" xmlns="http://www.w3.org/2000/svg">
    <rect width="540" height="307" fill="#ffffff"/>
    <path class="panel" d="M0 0 H288 Q350 120 367 307 H0 Z"/>
    <path class="swoosh" d="M288 0 H326 Q372 140 382 307 H367 Q350 120 288 0 Z"/>
    <path class="swoosh" d="M278 62 H312 Q352 110 366 170 L362 215 Q338 120 278 62 Z"/>
    <path class="flap-shade" d="M312 62 Q350 92 372 116 L372 146 Q350 110 320 80 Z"/>
    <text class="brand-name" x="26" y="166" font-size="76" textLength="252" lengthAdjust="spacingAndGlyphs">GLEAM</text>
    <text class="brand-tagline" x="28" y="198" font-size="20" textLength="250" lengthAdjust="spacingAndGlyphs">WINDOW CLEANING</text>
    <text class="placeholder" x="449" y="62" font-size="28" text-anchor="middle" letter-spacing="1">customer</text>
    <text class="placeholder" x="449" y="95" font-size="28" text-anchor="middle" letter-spacing="1">name</text>
  </svg>

  <!-- Back of card -->
  <svg class="card card--back" viewBox="0 0 540 307" xmlns="http://www.w3.org/2000/svg">
    <rect width="540" height="307" fill="#ffffff"/>
    <path class="panel" d="M0 214 Q270 178 540 196 V307 H0 Z"/>
    <path class="swoosh" d="M0 180 Q260 150 540 196 Q270 178 0 214 Z"/>
    <path class="swoosh" d="M84 228 L90 200 Q150 174 210 168 L210 182 Q150 190 84 228 Z"/>
    <path class="flap-shade" d="M98 198 Q146 176 210 170 L210 184 Q152 186 102 202 Z"/>
    <text class="placeholder" x="26" y="78" font-size="44" letter-spacing="1">Email</text>
    <text class="placeholder" x="26" y="130" font-size="44" letter-spacing="1">mobile</text>
    <text class="brand-name" x="305" y="262" font-size="64" textLength="210" lengthAdjust="spacingAndGlyphs">GLEAM</text>
    <text class="brand-tagline" x="306" y="289" font-size="17" textLength="209" lengthAdjust="spacingAndGlyphs">WINDOW CLEANING</text>
  </svg>

</main>
</body>
</html>
```